Business card for exciting VC company

Should look simple, crisp, and modern.

Industry/Entity Type

Venture Capital

Contact Information for Business Card

Would like to see at least one design that has our blue on the back with the tagline "Transforming Traditional Industry" and white front with contact details.

Font styles to use
Sans Serif

Requirements
Must have
• Logo

Gregory Tallis
gtallis@brindlewave.vc
Managing Partner
M (628)354-xxxx

```html
<!DOCTYPE html>
<html lang="en">
<head>
<meta charset="utf-8">
<title>Brindlewave Capital – Business Card</title>
<link href="https://fonts.googleapis.com/css2?family=Montserrat:wght@400;500;600&display=swap" rel="stylesheet">
<style>
  :root {
    --stage: #2b2d30;
    --card-white: #ffffff;
    --brand-blue: #3b79ba;
    --brand-blue-deep: #2f68a3;
    --ink: #141414;
    --ink-soft: #4a4a4a;
    --logo-light: #c9ccd2;
  }
  * { margin: 0; padding: 0; box-sizing: border-box; }
  html, body {
    width: 1200px; height: 900px; overflow: hidden;
    background: var(--stage);
    font-family: "Montserrat", Arial, sans-serif;
  }
  .stage {
    width: 1200px; height: 900px;
    display: flex; flex-direction: column;
    align-items: center; justify-content: center;
    gap: 56px;
  }
  .card {
    width: 630px; height: 360px;
    position: relative;
    box-shadow: 0 10px 30px rgba(0,0,0,.35);
  }
  .card-front { background: var(--card-white); }
  .card-back {
    background: linear-gradient(135deg, var(--brand-blue) 0%, var(--brand-blue-deep) 100%);
    display: flex; align-items: center; justify-content: center;
  }
  .wordmark {
    font-weight: 600;
    letter-spacing: 0.08em;
    text-transform: uppercase;
    white-space: nowrap;
  }
  .card-front .wordmark {
    position: absolute; left: 0; right: 0; top: 92px;
    text-align: center;
    font-size: 38px; color: var(--ink);
  }
  .card-back .wordmark { font-size: 40px; color: var(--logo-light); }
  .holder {
    position: absolute; left: 48px; top: 238px;
    width: 220px; text-align: right;
  }
  .holder-name {
    font-size: 15px; font-weight: 500; letter-spacing: .04em;
    text-transform: uppercase; color: var(--brand-blue);
  }
  .holder-title {
    margin-top: 4px; font-size: 14px; color: var(--ink-soft);
  }
  .divider {
    position: absolute; left: 292px; top: 232px;
    width: 2px; height: 58px; background: var(--brand-blue);
  }
  .contact {
    position: absolute; left: 316px; top: 236px;
    list-style: none; font-size: 14px; color: var(--ink-soft);
  }
  .contact-item { display: flex; align-items: center; gap: 10px; line-height: 26px; }
  .contact-icon { width: 14px; height: 14px; flex: none; }
</style>
</head>
<body>
<main class="stage">
  <section class="card card-front" aria-label="Card front">
    <div class="wordmark">Brindlewave Capital</div>
    <div class="holder">
      <p class="holder-name">Gregory Tallis</p>
      <p class="holder-title">Managing Partner</p>
    </div>
    <div class="divider"></div>
    <ul class="contact">
      <li class="contact-item">
        <svg class="contact-icon" viewBox="0 0 24 24" aria-hidden="true"><path fill="#3b79ba" d="M6.6 10.8a15 15 0 0 0 6.6 6.6l2.2-2.2a1 1 0 0 1 1-.25 11.4 11.4 0 0 0 3.6.57 1 1 0 0 1 1 1V20a1 1 0 0 1-1 1A17 17 0 0 1 3 4a1 1 0 0 1 1-1h3.5a1 1 0 0 1 1 1c0 1.25.2 2.45.57 3.6a1 1 0 0 1-.25 1z"/></svg>
        <span>(628)354-xxxx</span>
      </li>
      <li class="contact-item">
        <svg class="contact-icon" viewBox="0 0 24 24" aria-hidden="true"><rect x="2.5" y="5" width="19" height="14" rx="1.5" fill="none" stroke="#3b79ba" stroke-width="2"/><path d="M3 6l9 7 9-7" fill="none" stroke="#3b79ba" stroke-width="2"/></svg>
        <span>gtallis@brindlewave.vc</span>
      </li>
    </ul>
  </section>
  <section class="card card-back" aria-label="Card back">
    <div class="wordmark">Brindlewave Capital</div>
  </section>
</main>
</body>
</html>
```